Zine template for Velvet Orchard Zine

I wanted to create a zine template in inDesign or but could use some design expertise.  I have attached my draft doc.  the zine will sometimes be 32 pages, or 40 pages (8.5inches x 11, folded in 1/2). the publicaton is photocopied so placing pages in right order is important for easier assembly. I can attach sample.
I am open to masthead improvement (velvet orchard...pages you can touch).  But needs to look more like "hand made" -not too slick.  I am open to changing icon (pen dipping in water making waves...) to something that suggests a tactile, sensory impact.
I will fill in content myself for each edition.  But need page set ups that is column grid based.  So I can play with layout.  But wanted  a core based design that can make sure each edition is coherent.
Title page-same format but of course different theme, main pic, and contents
Letter from Editor/Table of Contents-again, format same, but content will change
Need 1 double page layout with double column layout option
1 double page layout with single column layout option
Maybe one with triple column layout option.
Common page number format-using shoe icon
I like idea of common theme based header or footer on each page
Add bus card info under Brindlewick press
Needs to have at least 1/2 inch margin around edges as it is copied and don't want content to bleed off page.
REmember pages stapled so need enough space between columns in middle to allow for staple and still read content
DOes this make sense?  Essentially looking for a mag layout for zine (which is just using std letter size paper, folder, and stapled to make a zine (like a pamphlet).  I uploaded a few samples of layouts and how the pages work.
Let me know if you have questions!

```html
<!DOCTYPE html>
<html lang="en">
<head>
<meta charset="utf-8">
<title>Velvet Orchard Zine – Spread Template</title>
<link rel="stylesheet" href="https://fonts.googleapis.com/css2?family=Rye&family=PT+Mono&family=Roboto+Mono:wght@700&display=swap">
<style>
  :root {
    --backdrop: #e4e4e2;
    --page-blue: #5aaee6;
    --field-green: #8cbf3a;
    --cover-orange: #d4793a;
    --tab-yellow: #f2d43c;
    --strip-white: #ffffff;
    --ink: #2a2a2a;
    --title-blue: #3d8fd1;
    --sky-top: #7fa8dc;
    --sky-mid: #dfe9f4;
    --grass: #7fbf3a;
    --grass-deep: #5a9a26;
  }
  * { box-sizing: border-box; margin: 0; padding: 0; }
  html, body { width: 1200px; height: 800px; overflow: hidden; }
  body { background: var(--backdrop); font-family: "PT Mono", monospace; color: var(--ink); }

  .spread { position: absolute; left: 80px; top: 110px; width: 1040px; height: 580px; box-shadow: 0 6px 18px rgba(0,0,0,.18); }
  .page { position: absolute; top: 0; height: 580px; overflow: hidden; }
  .page--back { left: 0; width: 200px; background: var(--cover-orange); }
  .page--left { left: 200px; width: 420px; background: var(--page-blue); border-left: 2px solid #fff; }
  .page--right { left: 620px; width: 420px; background: var(--page-blue); box-shadow: inset 14px 0 16px -12px rgba(0,0,0,.25); }

  .strip { font-size: 9px; line-height: 1.6; }
  .strip span { background: var(--strip-white); padding: 1px 3px; -webkit-box-decoration-break: clone; box-decoration-break: clone; }

  .running-head { position: absolute; font-size: 7px; letter-spacing: .08em; text-transform: uppercase; }
  .running-head span { background: var(--strip-white); padding: 0 3px; }
  .running-head .section { background: var(--tab-yellow); }
  .folio { position: absolute; bottom: 12px; font-size: 7px; letter-spacing: .1em; }
  .folio span { background: var(--tab-yellow); padding: 1px 4px; }

  .photo {
    position: absolute; border: 4px solid #fff;
    background: linear-gradient(180deg, var(--sky-top) 0%, var(--sky-mid) 45%, var(--grass) 60%, var(--grass-deep) 100%);
    box-shadow: 1px 2px 4px rgba(0,0,0,.25);
  }

  /* back page */
  .back-photo { position: absolute; left: 0; top: 18px; width: 200px; height: 172px;
    background: linear-gradient(180deg, var(--sky-top) 0%, var(--sky-mid) 48%, var(--grass) 62%, var(--grass-deep) 100%); }
  .back-band { position: absolute; left: 0; top: 190px; width: 200px; height: 72px; background: var(--field-green);
    display: flex; align-items: center; padding-left: 36px; }
  .back-band h2 { font-family: "Rye", serif; font-weight: 400; font-size: 17px; line-height: 1.15; color: #f4e98a; letter-spacing: .04em; }
  .directory { position: absolute; left: 52px; top: 278px; width: 140px; }
  .directory .strip { margin-bottom: 10px; font-size: 8px; }

  /* left page */
  .headline { position: absolute; left: 22px; top: 24px; font-family: "Rye", serif; font-weight: 400; font-size: 38px; line-height: 1.08; color: var(--field-green); }
  .headline span { background: var(--strip-white); padding: 0 6px; -webkit-box-decoration-break: clone; box-decoration-break: clone; }
  .intro { position: absolute; left: 22px; top: 172px; width: 380px; font-size: 10px; line-height: 1.6; font-weight: 700; }
  .intro span { background: var(--tab-yellow); padding: 1px 3px; -webkit-box-decoration-break: clone; box-decoration-break: clone; }

  /* numbered features */
  .feature { position: absolute; }
  .feature__num { display: inline-block; background: var(--tab-yellow); font-family: "Roboto Mono", monospace; font-weight: 700; font-size: 19px; line-height: 1; padding: 3px 5px; color: var(--ink); float: left; margin: 0 5px 2px 0; }
  .feature__title { font-size: 8.5px; font-weight: 700; color: var(--title-blue); text-transform: uppercase; line-height: 1.65; }
  .feature__title span { background: var(--strip-white); padding: 1px 3px; -webkit-box-decoration-break: clone; box-decoration-break: clone; }
  .feature__body { clear: both; margin-top: 2px; }
  .feature--lead .feature__num { font-size: 24px; }
  .feature--lead .strip { font-size: 9.5px; }
</style>
</head>
<body>
<main class="spread">

  <section class="page page--back">
    <div class="running-head" style="left:20px;top:5px"><span>velvet orchard</span> <span class="section">section name</span></div>
    <div class="back-photo" role="img" aria-label="Photo of a green hill with a lone tree under a blue sky"></div>
    <div class="back-band"><h2>ANOTHER<br>LINE HERE</h2></div>
    <div class="directory">
      <p class="strip"><span>Drift Lantern<br>212 Quillfeather Lane<br>Marrow Bay, CA 90000<br>Phone: 555-014-2290</span></p>
      <p class="strip"><span>Hollowpine Travel<br>48 Copperleaf Road<br>Fernwick, CO 80000<br>Phone: 555-013-7741</span></p>
      <p class="strip"><span>Lark &amp; Ember Trips<br>907 Mossgate Street<br>Tilbury, PA 19000<br>Phone: 555-018-3356</span></p>
      <p class="strip"><span>Far Corners Guide<br>31 Bramblewood Road<br>Ashcombe, WI 53000<br>Phone: 555-017-6624</span></p>
    </div>
    <div class="folio" style="left:80px"><span>VOLUME 1</span></div>
  </section>

  <section class="page page--left">
    <h1 class="headline"><span>YOUR<br>HEADING<br>GOES HERE!</span></h1>
    <p class="intro"><span>Magazine template. We have plenty of space here and can start with any long line up to three full lines of text.</span></p>
    <div class="photo" style="left:40px;top:238px;width:330px;height:170px;transform:rotate(-4deg)" role="img" aria-label="Photo of a rolling green hill with a single tree and white clouds"></div>

    <article class="feature feature--lead" style="left:22px;top:440px;width:185px">
      <span class="feature__num">01</span>
      <p class="feature__title"><span>Ink that stains the fingers</span></p>
      <p class="feature__body strip"><span>Each copy passes through our hands before it reaches yours, folded, pressed and stapled at the same old table.</span></p>
    </article>
    <article class="feature feature--lead" style="left:215px;top:428px;width:190px">
      <span class="feature__num">02</span>
      <p class="feature__title"><span>Paper worn soft at corners</span></p>
      <p class="feature__body strip"><span>Turn the pages slowly. Some were photocopied twice, some carry a smudge we chose to keep for you.</span></p>
    </article>
  </section>

  <section class="page page--right">
    <div class="running-head" style="left:300px;top:5px"><span class="section">section name</span> <span>velvet orchard</span></div>

    <div class="photo" style="left:16px;top:44px;width:118px;height:88px;transform:rotate(-8deg)" role="img" aria-label="Photo of a green hill with a lone tree"></div>
    <article class="feature" style="left:150px;top:28px;width:125px">
      <span class="feature__num">07</span>
      <p class="feature__title"><span>Stitched by kitchen light</span></p>
      <p class="feature__body strip"><span>Thread, needle and a lamp that hums while the pages find their order.</span></p>
    </article>
    <article class="feature" style="left:285px;top:20px;width:125px">
      <span class="feature__num">18</span>
      <p class="feature__title"><span>Notes from the back room</span></p>
      <p class="feature__body strip"><span>What the editor scribbled between deadlines, kept here without much tidying.</span></p>
    </article>
    <article class="feature" style="left:150px;top:145px;width:125px">
      <span class="feature__num">11</span>
      <p class="feature__title"><span>Glue, scissors and patience</span></p>
      <p class="feature__body strip"><span>Every collage starts as a mess on the floor and ends up here.</span></p>
    </article>
    <article class="feature" style="left:285px;top:135px;width:125px">
      <span class="feature__num">21</span>
      <p class="feature__title"><span>A letter left unsent</span></p>
      <p class="feature__body strip"><span>Words written late at night to a friend who moved far away.</span></p>
    </article>
    <article class="feature" style="left:14px;top:192px;width:125px">
      <span class="feature__num">03</span>
      <p class="feature__title"><span>Small press, loud heart</span></p>
      <p class="feature__body strip"><span>How a few people with one copier keep printing every single season.</span></p>
    </article>
    <div class="photo" style="left:150px;top:258px;width:125px;height:86px;transform:rotate(-3deg)" role="img" aria-label="Photo of a grassy hill with a tree and clouds"></div>
    <article class="feature" style="left:285px;top:255px;width:125px">
      <span class="feature__num">30</span>
      <p class="feature__title"><span>The last page first</span></p>
      <p class="feature__body strip"><span>Start at the end and read backwards, the story still holds together.</span></p>
    </article>
    <article class="feature" style="left:14px;top:330px;width:125px">
      <span class="feature__num">04</span>
      <p class="feature__title"><span>Rain on the window</span></p>
      <p class="feature__body strip"><span>Quiet sounds recorded on paper for the days you stay inside.</span></p>
    </article>
    <article class="feature" style="left:150px;top:365px;width:125px">
      <span class="feature__num">16</span>
      <p class="feature__title"><span>Maps drawn from memory</span></p>
      <p class="feature__body strip"><span>Streets we walked as children, sketched again from what we remember.</span></p>
    </article>
    <div class="photo" style="left:285px;top:385px;width:122px;height:86px;transform:rotate(-6deg)" role="img" aria-label="Photo of a green hill with a lone tree"></div>
    <article class="feature" style="left:80px;top:470px;width:140px">
      <span class="feature__num">05</span>
      <p class="feature__title"><span>Songs for slow mornings</span></p>
      <p class="feature__body strip"><span>A short playlist and a few lines about why each one matters.</span></p>
    </article>

    <div class="folio" style="right:14px"><span>VOLUME 1</span></div>
  </section>

</main>
</body>
</html>
```